Bramwell Joinery Website

My client Bramwell Joinery is looking for a redesign for a Word Press Website. Their current site is at www.bramwelljoinery.example They are a custom cabinet company, but also create bathroom, living room, bar and entertainment and bedroom cabinets too. They would like a design that emulates the master craftsman work they do yet a contemporary style.

Their current site was designed using Flash elements.

Target Market(s)

Home owners and builders of high end homes

Industry/Entity Type

Entertainment

Font styles to use
Serif
Decorative

Requirements
Must have
• Must show their work and logo using a contemporary style.
Nice to have
• Sliders that showcase their projects.

```html
<!DOCTYPE html>
<html lang="en">
<head>
<meta charset="utf-8">
<title>Bramwell Joinery</title>
<link rel="stylesheet" href="https://fonts.googleapis.com/css2?family=Noto+Serif:ital,wght@0,400;1,400&family=Mulish:wght@400;600;700&display=swap">
<style>
  :root {
    --green: #3cb43a;
    --green-light: #56c84a;
    --green-dark: #2a9a2c;
    --panel: #f2f2f2;
    --panel-border: #cfcfcf;
    --ink: #111;
    --body-text: #444;
    --footer-bg: #161718;
    --footer-text: #c9c9c9;
    --white: #fff;
    --photo-warm: #b8a58e;
    --photo-dark: #4a3a30;
  }
  * { margin: 0; padding: 0; box-sizing: border-box; }
  html, body { width: 1200px; height: 1166px; overflow: hidden; }
  body { position: relative; background: var(--white); font-family: "Mulish", sans-serif; color: var(--ink); }
  .abs { position: absolute; }

  .utility-nav { top: 12px; left: 682px; display: flex; align-items: center; font-size: 13px; color: var(--ink); }
  .utility-nav span.sep { margin: 0 15px; font-size: 11px; }
  .utility-social { top: 10px; left: 998px; display: flex; gap: 12px; }
  .utility-social i { display: block; width: 17px; height: 17px; border-radius: 50%; background: #444; }

  .green-band { top: 40px; left: 0; width: 1200px; height: 112px;
    background: linear-gradient(180deg, var(--green-light), var(--green) 50%, var(--green-dark)); }
  .green-inner { top: 38px; left: 124px; width: 956px; height: 106px;
    background: linear-gradient(180deg, #5bd04f, var(--green) 55%, #2f9f2f);
    box-shadow: 0 3px 6px rgba(0,0,0,.25); }
  .main-nav { top: 78px; left: 355px; display: flex; gap: 33px; font-family: "Noto Serif", serif; font-size: 19px; color: var(--white); }

  .logo-tab { top: 0; left: 147px; width: 164px; height: 168px; background: var(--white);
    border-radius: 0 0 82px 82px; box-shadow: 0 2px 5px rgba(0,0,0,.2);
    display: flex; flex-direction: column; align-items: center; justify-content: center; gap: 8px; }
  .logo-tab .dot { width: 40px; height: 40px; border-radius: 50%; background: var(--green); }
  .logo-tab .name { font-family: "Noto Serif", serif; font-size: 17px; color: var(--ink); text-align: center; line-height: 1.2; }

  .content-panel { top: 152px; left: 135px; width: 935px; height: 738px; background: var(--panel);
    border: 1px solid var(--panel-border); border-top: 0; }
  .hero { top: 163px; left: 146px; width: 914px; height: 357px;
    background: linear-gradient(90deg, #d9d2c6 0%, #c9b9a4 40%, #8a7868 70%, var(--photo-dark) 100%); }
  .hero-caption { top: 278px; left: 147px; width: 372px; height: 123px; background: rgba(20,20,20,.72);
    font-family: "Noto Serif", serif; font-style: italic; color: var(--white); font-size: 33px; line-height: 37px; padding: 22px 0 0 17px; }

  .thumb { top: 530px; width: 176px; height: 86px;
    background: linear-gradient(90deg, #d8cfc2, var(--photo-warm) 60%, #6a5646); }
  .thumb.active { background: #2e2e2e; border: 3px solid var(--green); }
  .slider-arrow { top: 549px; width: 30px; height: 48px; background: rgba(20,20,20,.8); }
  .slider-arrow.prev { left: 146px; border-radius: 0 24px 24px 0; }
  .slider-arrow.next { left: 1030px; border-radius: 24px 0 0 24px; }
  .slider-arrow svg { position: absolute; top: 15px; }

  .section-title { font-family: "Noto Serif", serif; font-size: 25px; color: var(--ink); }
  .about-text { top: 700px; left: 153px; width: 595px; font-size: 14.5px; line-height: 25px; color: var(--body-text); }

  .video-frame { top: 693px; left: 762px; width: 298px; height: 164px; background: var(--white); box-shadow: 0 1px 3px rgba(0,0,0,.25); }
  .video-still { top: 697px; left: 770px; width: 283px; height: 136px; background: linear-gradient(90deg, #3a3a3a, #8c8072 50%, #cfc4b4); }
  .video-bar { top: 833px; left: 770px; width: 283px; height: 18px; background: #1b1b1b; }
  .video-progress { top: 831px; left: 770px; width: 52px; height: 3px; background: #d42020; }
  .play-btn { top: 746px; left: 885px; width: 60px; height: 38px; background: rgba(10,10,10,.85); }

  .footer { top: 890px; left: 0; width: 1200px; height: 276px; background: var(--footer-bg); }
  .footer-title { font-size: 16px; font-weight: 700; color: var(--white); }
  .sitemap { top: 973px; left: 151px; list-style: none; font-size: 13.5px; line-height: 22px; color: var(--footer-text); }
  .sitemap li::before { content: "\2022"; color: var(--white); margin-right: 5px; }
  .contact-line { left: 333px; display: flex; gap: 8px; font-size: 13.5px; line-height: 22px; color: var(--footer-text); }
  .contact-line svg { flex: none; margin-top: 5px; }
  .follow-icons { top: 981px; left: 660px; display: flex; gap: 11px; }
  .follow-icons i { display: block; width: 25px; height: 25px; border-radius: 50%; }
  .brand-line { top: 1031px; left: 656px; display: flex; align-items: center; gap: 9px; font-size: 17px; font-weight: 700; color: var(--white); }
  .brand-line i { width: 20px; height: 20px; border-radius: 50%; background: #8a8a8a; display: block; }
  .copyright { top: 1066px; left: 660px; font-size: 13.5px; line-height: 20px; color: var(--footer-text); }
  .footer-badge { top: 965px; left: 922px; width: 126px; height: 126px; border-radius: 50%; border: 3px solid #6a6a6a; }
</style>
</head>
<body>
  <nav class="abs utility-nav">
    <span>Getting Started</span><span class="sep">|</span><span>Who We Are</span><span class="sep">|</span><span>Contact Us</span>
  </nav>
  <div class="abs utility-social"><i></i><i></i><i></i></div>

  <div class="abs green-band"></div>
  <div class="abs green-inner"></div>
  <nav class="abs main-nav">
    <span>Home</span><span>Customer Experience</span><span>Professional</span><span>Portfolio</span><span>Cabinet Hardware</span>
  </nav>
  <div class="abs logo-tab">
    <span class="dot"></span>
    <span class="name">Bramwell<br>Joinery</span>
  </div>

  <div class="abs content-panel"></div>
  <div class="abs hero" role="img" aria-label="Photo of a finished kitchen with white and dark wood cabinets"></div>
  <div class="abs hero-caption">Welcome to Bramwell<br>Joinery &amp; Fixtures</div>

  <div class="abs thumb" style="left:146px" role="img" aria-label="Project photo: built-in oven cabinetry"></div>
  <div class="abs thumb active" style="left:330px" role="img" aria-label="Project photo: dark kitchen"></div>
  <div class="abs thumb" style="left:515px" role="img" aria-label="Project photo: white kitchen with island"></div>
  <div class="abs thumb" style="left:700px" role="img" aria-label="Project photo: kitchen with pendant lights"></div>
  <div class="abs thumb" style="left:885px" role="img" aria-label="Project photo: kitchen with glass cabinets"></div>
  <div class="abs slider-arrow prev"><svg width="16" height="18" viewBox="0 0 16 18" style="left:5px"><path d="M12 2 L4 9 L12 16" stroke="#fff" stroke-width="3" fill="none"/></svg></div>
  <div class="abs slider-arrow next"><svg width="16" height="18" viewBox="0 0 16 18" style="left:9px"><path d="M4 2 L12 9 L4 16" stroke="#fff" stroke-width="3" fill="none"/></svg></div>

  <h2 class="abs section-title" style="top:648px;left:152px">WHO WE ARE</h2>
  <p class="abs about-text">Established in 1966, Bramwell Joinery has long stood as one of the Midwest's most renowned makers of custom cabinets and fixtures. Our handcrafted, award-winning creations have been chosen by hundreds of noteworthy homebuilders. And while we custom build cabinets, we built our business around the belief that our customers absolutely, unequivocally come first. From day one, our mission has been to help turn the houses that people live in to the homes they've always dreamed of.</p>

  <h2 class="abs section-title" style="top:648px;left:766px">WATCH OUR VIDEO</h2>
  <div class="abs video-frame"></div>
  <div class="abs video-still" role="img" aria-label="Video still of cabinetry with a built-in oven"></div>
  <div class="abs video-bar"></div>
  <div class="abs video-progress"></div>
  <div class="abs play-btn"><svg width="60" height="38" viewBox="0 0 60 38"><path d="M24 11 L37 19 L24 27 Z" fill="#fff"/></svg></div>

  <footer class="abs footer"></footer>
  <h3 class="abs footer-title" style="top:936px;left:151px">Site Map</h3>
  <ul class="abs sitemap">
    <li>Home</li><li>Who We Are</li><li>Getting Started</li><li>Customer Experience</li><li>Professional</li><li>Portfolio</li>
  </ul>

  <h3 class="abs footer-title" style="top:936px;left:332px">Contact us</h3>
  <div class="abs contact-line" style="top:972px">
    <svg width="14" height="17" viewBox="0 0 14 17"><path d="M7 0 C3 0 0 3 0 7 C0 11 7 17 7 17 C7 17 14 11 14 7 C14 3 11 0 7 0 Z M7 4 A3 3 0 1 1 7 10 A3 3 0 1 1 7 4 Z" fill="#777"/></svg>
    <span>Bramwell Joinery Tom Harlow<br>4820 E. Linden Avenue Fairview,<br>MO 64120</span>
  </div>
  <div class="abs contact-line" style="top:1053px">
    <svg width="14" height="15" viewBox="0 0 14 15"><path d="M2 0 L5 0 L6 4 L4 6 C5 9 6 10 9 11 L11 9 L14 10 L14 13 C14 14 13 15 12 15 C5 14 0 9 0 2 C0 1 1 0 2 0 Z" fill="#777"/></svg>
    <span>555.014.2300</span>
  </div>
  <div class="abs contact-line" style="top:1087px">
    <svg width="16" height="12" viewBox="0 0 16 12"><rect x="0.5" y="0.5" width="15" height="10" fill="none" stroke="#777"/><path d="M1 1 L8 7 L15 1" stroke="#777" fill="none"/></svg>
    <span>info@bramwell.example</span>
  </div>

  <h3 class="abs footer-title" style="top:936px;left:660px">Follow Us</h3>
  <div class="abs follow-icons">
    <i style="background:#3b5998"></i><i style="background:#1d8ecb"></i><i style="background:#e8632a"></i><i style="background:#c0262d"></i>
  </div>
  <div class="abs brand-line"><i></i><span>BRAMWELL</span></div>
  <p class="abs copyright">copyright©2015.Bramwell Joinery<br>All Rights Reserved</p>
  <div class="abs footer-badge"></div>
</body>
</html>
```